New Pain Management Physcian Private Practice webpage design

Interventional Pain Management Company looking for new website. Want it modeled very closely to http://www.brightveloclinic.example/ website. Under navigation panel at top of main webpage take off the following tabs: About, Locations, News, Testimonial, and Pain Channel. Add New Patient visit tab, change about to Main Page, change treatments to Procedures, change Providers to Provider.Main web page should have the KTR logo, no picture slideshow for now but want ability to add pictures to the slideshow in the future. Pictures are included to show you an idea of what main page should look like. Colors are teal,Deep Navy, and White as shown in KTR logo. Font style should also be same as KTR logo.

Target Market(s)

Patients with all kinda of acute and chronic pain. Especially neck, mid back,low back pain, and joint pain.

Industry/Entity Type

Medical

Coding

Coded - Design and coding required

Number of Pages Required

5+ page

Requirements
Must have
• See Project description above
Nice to have
• ability to add pictures to the slideshow in future
Should not have
• not applicable

```html
<!DOCTYPE html>
<html lang="en">
<head>
<meta charset="utf-8">
<title>Kestra Total Relief — Pain Management</title>
<link rel="stylesheet" href="https://fonts.googleapis.com/css2?family=Michroma&family=Lato:ital,wght@0,400;0,700;0,900;1,400&display=swap">
<style>
:root{
  --teal:#5f9aa4;
  --teal-dark:#4d8791;
  --navy:#1d2a45;
  --navy-btn:#26344f;
  --ink:#333a44;
  --link:#2f4f86;
  --muted:#5c6470;
  --rule:#d9dde2;
  --white:#ffffff;
  --footer:#141414;
}
*{box-sizing:border-box;margin:0;padding:0}
html,body{width:1200px;height:2195px;overflow:hidden}
body{font-family:"Lato",Arial,sans-serif;color:var(--ink);background:var(--white);position:relative}
ul{list-style:none}
.display{font-family:"Michroma","Lato",sans-serif;letter-spacing:3px}

/* Header */
.site-header{position:absolute;top:0;left:0;width:1200px;height:128px;background:var(--teal)}
.brand{position:absolute;left:88px;top:62px;display:flex;align-items:center;gap:12px}
.brand-mark{width:46px;height:46px;background:var(--navy);border:2px solid var(--white)}
.brand-name{font-family:"Michroma",sans-serif;color:var(--white);font-size:18px;line-height:1.25;letter-spacing:2px}
.enquiry{position:absolute;right:85px;top:16px;color:var(--white);font-size:13px;font-weight:700;letter-spacing:.5px}
.search{position:absolute;right:85px;top:48px;display:flex}
.search-field{width:215px;height:32px;background:var(--white);font-size:11px;color:#8a8f96;padding:9px 10px}
.search-btn{width:66px;height:32px;background:var(--teal-dark);color:var(--white);font-size:11px;font-weight:700;display:flex;align-items:center;justify-content:center}
.utility{position:absolute;right:85px;top:97px;display:flex;gap:22px;color:var(--white);font-size:11.5px;font-weight:700}

/* Nav */
.main-nav{position:absolute;top:128px;left:0;width:1200px;height:34px;background:var(--white);border-bottom:1px solid var(--rule)}
.main-nav ul{display:flex;gap:36px;padding-left:88px;height:34px;align-items:center;font-size:12.5px;font-weight:700;color:#222}

/* Hero */
.hero{position:absolute;top:162px;left:0;width:1200px;height:434px;background:linear-gradient(100deg,#c9b8a0 0%,#8f8a78 30%,#b6c6c2 55%,#6f7e77 80%,#4c5b52 100%)}
.hero-shade{position:absolute;right:0;top:0;width:640px;height:434px;background:linear-gradient(90deg,rgba(0,0,0,0),rgba(20,30,40,.35))}
.hero-copy{position:absolute;left:568px;top:135px;width:560px;color:var(--white)}
.hero-kicker{font-size:21px;margin-bottom:6px}
.hero-title{font-size:27px;margin-bottom:14px}
.hero-text{font-size:13.5px;line-height:1.55}
.btn{display:inline-flex;align-items:center;gap:8px;background:var(--navy-btn);color:var(--white);font-size:12px;font-weight:700;height:40px;padding:0 22px}
.hero .btn{margin-top:20px}

/* Sections */
.section-title{font-size:19px;color:var(--navy)}
.section-sub{font-size:13.5px;color:var(--link);margin-top:10px}

.about{position:absolute;top:640px;left:85px;width:1030px}
.about-photo{position:absolute;top:77px;left:0;width:240px;height:246px;background:linear-gradient(160deg,#b8a48e,#3e3a3a 60%,#1c1f26)}
.about-text{position:absolute;top:77px;left:264px;width:766px;font-size:13.2px;line-height:1.72;color:var(--ink)}
.about-text p{margin-bottom:2px}
.read-more{display:inline-block;margin-top:8px;font-size:13.5px;color:var(--ink)}

.news{position:absolute;top:1018px;left:85px;width:1030px}
.news-grid{position:absolute;top:70px;left:0;display:flex;gap:28px}
.news-card{width:325px;text-align:center}
.news-photo{width:325px;height:212px}
.news-title{font-size:13px;font-weight:900;letter-spacing:2px;color:#222;margin-top:20px}
.news-text{font-size:12.5px;font-style:italic;color:var(--muted);line-height:1.65;margin-top:10px}
.news-card .read-more{margin-top:8px}

/* Testimonial band */
.testimonial{position:absolute;top:1440px;left:0;width:1200px;height:316px;background:linear-gradient(90deg,#3d5a5c,#5d7f7f 45%,#4a6a6b 70%,#2f4646);color:var(--white);text-align:center}
.testimonial-title{font-family:"Lato",sans-serif;font-size:25px;letter-spacing:4px;line-height:1.45;padding-top:68px}
.testimonial-title strong{font-weight:900}
.testimonial-text{width:800px;margin:16px auto 0;font-size:13px;font-style:italic;line-height:1.6}
.testimonial .btn{margin-top:30px;background:var(--teal);height:40px}

/* Treatments */
.treatments{position:absolute;top:1772px;left:88px;width:1030px}
.treatments-title{font-size:13.5px;color:var(--navy);letter-spacing:2px}
.treatment-cols{position:absolute;top:52px;left:0;display:flex}
.treatment-cols ul{font-size:12px;line-height:1.7;color:var(--link)}
.treatment-cols ul:nth-child(1){width:161px}
.treatment-cols ul:nth-child(2){width:198px}
.treatment-cols ul:nth-child(3){width:163px}
.treatment-cols ul:nth-child(4){width:171px}

/* Footer */
.site-footer{position:absolute;top:1928px;left:0;width:1200px;height:267px;background:var(--footer);color:var(--white)}
.footer-heading{font-size:13px;font-weight:900;letter-spacing:.5px}
.footer-col{position:absolute;top:32px}
.footer-links{display:flex;gap:50px;margin-top:30px}
.footer-links ul{font-size:11.5px;line-height:2.15;width:100px}
.footer-links ul+ul{width:160px}
.footer-text{font-size:11.5px;line-height:2;margin-top:30px;width:370px;letter-spacing:.3px}
.footer-hours{font-size:11.5px;line-height:2.05;margin-top:30px;width:260px}
.social{display:flex;gap:10px;margin-top:12px}
.social span{width:32px;height:32px;border-radius:50%;background:#4a4a4a}
.copyright{font-size:11.5px;margin-top:14px}
</style>
</head>
<body>

<header class="site-header">
  <div class="brand">
    <div class="brand-mark"></div>
    <div class="brand-name">KESTRA<br>TOTAL RELIEF</div>
  </div>
  <div class="enquiry">CALL US FOR ENQUIRY: &nbsp;(555) 0142-7710</div>
  <div class="search">
    <div class="search-field">Search for detail</div>
    <div class="search-btn">SEARCH</div>
  </div>
  <div class="utility">
    <span>WATCH TREATMENT VIDEOS</span><span>MY PORTAL</span><span>REQUEST AN APPOINTMENT</span>
  </div>
</header>

<nav class="main-nav">
  <ul>
    <li>HOME</li><li>MAIN PAGE</li><li>LOCATIONS</li><li>NEWS</li><li>TESTIMONIAL</li><li>PAIN CHANNEL</li><li>PROCEDURES</li><li>PROVIDER</li><li>NEW PATIENT VISIT</li>
  </ul>
</nav>

<section class="hero" role="img" aria-label="Photo of a runner on a sunny road holding her injured knee">
  <div class="hero-shade"></div>
  <div class="hero-copy">
    <div class="hero-kicker display">LOREM IPSUM DOLOR</div>
    <div class="hero-title display">CONSEC TETUR ADIPISICIN</div>
    <p class="hero-text">Lorem ipsum dolor sit amet, consectetur adipisicing elit, sed do eiusmod tempor incididunt ut labore et dolore magna aliqua. Ut enim ad minim veniam, Duis aute irure dolor in reprehenderit in voluptate velit esse cillum dolore eu fugiat nulla pariatur. Excepteur sint</p>
    <span class="btn">
      <svg width="10" height="10" viewBox="0 0 10 10"><path d="M2 1 L8 5 L2 9 Z" fill="#fff"/></svg>EXPLORE MORE
    </span>
  </div>
</section>

<section class="about">
  <h2 class="section-title display">ABOUT KTR</h2>
  <p class="section-sub">Duis aute irure dolor in reprehenderit in voluptate velit esse cillum</p>
  <div class="about-photo" role="img" aria-label="Portrait photo of the practice physician in a dark suit"></div>
  <div class="about-text">
    <p>Sed ut perspiciatis unde omnis iste natus error sit voluptatem accusantium doloremque laudantium, totam rem aperiam, eaque ipsa quae ab illo inventore veritatis et quasi architecto beatae vitae dicta sunt explicabo. Nemo enim ipsam voluptatem quia voluptas sit aspernatur aut odit aut fugit, sed quia consequuntur magni dolores eos qui ratione voluptatem sequi nesciunt.</p>
    <p>Sed ut perspiciatis unde omnis iste natus error sit voluptatem accusantium doloremque laudantium, totam rem aperiam, eaque ipsa quae ab illo inventore veritatis et quasi architecto beatae vitae dicta sunt explicabo. Nemo enim ipsam voluptatem quia voluptas sit aspernatur aut odit aut fugit, sed quia consequuntur magni dolores eos qui ratione voluptatem sequi nesciunt.</p>
    <p>Sed ut perspiciatis unde omnis iste natus error sit voluptatem accusantium doloremque laudantium, totam rem aperiam, eaque ipsa quae ab illo inventore veritatis et quasi architecto beatae vitae dicta sunt explicabo. Nemo enim ipsam voluptatem quia voluptas sit aspernatur aut odit aut fugit, sed quia consequuntur magni dolores eos qui ratione voluptatem sequi nesciunt.</p>
    <span class="read-more">Read More &rsaquo;</span>
  </div>
</section>

<section class="news">
  <h2 class="section-title display">LATEST NEWS</h2>
  <p class="section-sub">Duis aute irure dolor in reprehenderit in voluptate velit esse cillum</p>
  <div class="news-grid">
    <article class="news-card">
      <div class="news-photo" role="img" aria-label="Photo of a runner holding his knee on a garden path" style="background:linear-gradient(150deg,#c7d48f,#6a8f3c 55%,#3f5f2a)"></div>
      <h3 class="news-title">NEQUE PORRO QUISQUAM EST</h3>
      <p class="news-text">Quis autem vel eum iure reprehenderit qui in ea voluptate velit esse quam nihil molestiae consequatur</p>
      <span class="read-more">Read More &rsaquo;</span>
    </article>
    <article class="news-card">
      <div class="news-photo" role="img" aria-label="Photo of a man on a sofa holding his lower back" style="background:linear-gradient(150deg,#e6e3dc,#b8b2a6 55%,#4a5770)"></div>
      <h3 class="news-title">NEQUE PORRO QUISQUAM EST</h3>
      <p class="news-text">Quis autem vel eum iure reprehenderit qui in ea voluptate velit esse quam nihil molestiae consequatur</p>
      <span class="read-more">Read More &rsaquo;</span>
    </article>
    <article class="news-card">
      <div class="news-photo" role="img" aria-label="Photo of a man sitting on a bed holding his neck" style="background:linear-gradient(150deg,#f1eee8,#d7cfc3 50%,#9a7c62)"></div>
      <h3 class="news-title">NEQUE PORRO QUISQUAM EST</h3>
      <p class="news-text">Quis autem vel eum iure reprehenderit qui in ea voluptate velit esse quam nihil molestiae consequatur</p>
      <span class="read-more">Read More &rsaquo;</span>
    </article>
  </div>
</section>

<section class="testimonial" role="img" aria-label="Background photo of a hiker on a wooded trail">
  <h2 class="testimonial-title">EVERYONE'S ADVENTURE IS DIFFERENT<br>BUT THEY SHOULD ALL BE <strong>WITHOUT PAIN</strong></h2>
  <p class="testimonial-text">Temporibus autem quibusdam et aut officiis debitis aut rerum necessitatibus saepe eveniet ut et voluptates repudiandae sint et molestiae non recusandae.Itaque earum rerum hic tenetur a sapiente delectus</p>
  <span class="btn">READ PATIENT TESTIMONIALS</span>
</section>

<section class="treatments">
  <h2 class="treatments-title display">THE LEADING MEDICAL TREATMENTS FOR PAIN</h2>
  <div class="treatment-cols">
    <ul><li>BACK PAIN</li><li>NECK PAIN</li><li>FACE PAIN</li><li>ARTHRITIS PAIN</li></ul>
    <ul><li>POST-SURGICAL PAIN</li><li>POST-TRAUMA PAIN</li><li>PHANTOM LIMB PAIN</li><li>HEADACHES</li></ul>
    <ul><li>CANCER PAIN</li><li>PAINFUL DISCS</li><li>SHINGLES</li><li>FIBROMYALGIA</li></ul>
    <ul><li>MID BACK</li><li>LOW BACK PAIN</li><li>JOINT PAIN</li><li>SPORTS INJURIES</li></ul>
    <ul><li>POST-SURGICAL PAIN</li><li>POST-TRAUMA PAIN</li><li>PHANTOM LIMB PAIN</li><li>HEADACHES</li></ul>
  </div>
</section>

<footer class="site-footer">
  <div class="footer-col" style="left:88px">
    <h3 class="footer-heading">QUICK LINKS</h3>
    <div class="footer-links">
      <ul><li>HOME</li><li>ABOUT</li><li>LOCATIONS</li><li>NEWS</li><li>TESTIMONIAL</li><li>PAIN CHANNEL</li><li>PATIENT VISIT</li></ul>
      <ul><li>MEET THE PROVIDERS</li><li>PATIENT FORMS</li><li>FAQ</li><li>ACCEPTED INSURANCE</li><li>REQUEST APPOINTMENT</li><li>PROCEDURES</li><li>PROVIDER</li></ul>
    </div>
  </div>
  <div class="footer-col" style="left:456px">
    <h3 class="footer-heading">MANAGE YOUR PAIN AND GET BACK INTO LIFE.</h3>
    <p class="footer-text">TEMPORIBUS AUTEM QUIBUSDAM ET AUT OFFICIIS DEBITIS AUT RERUM NECESSITATIBUS SAEPE EVENIET UT ET VOLUPTATES REPUDIANDAE SINT ET MOLESTIAE NON RECUSANDAE. ITAQUE EARUM RERUM HIC TENETUR A SAPIENTE DELECTUS, UT AUT REICIENDIS VOLUPTATIBUS MAIORES ALIAS CONSEQUATUR AUT PERFERENDIS DOLORIBUS ASPERIORES REPELLAT</p>
  </div>
  <div class="footer-col" style="left:861px">
    <h3 class="footer-heading">OFFICE LOCATION</h3>
    <p class="footer-hours">M-F &nbsp;08.00 AM - 5.00 PM<br>OFFICE CLOSED FROM 11.00 AM - 1.00 PM<br>DAILY</p>
    <div class="social" aria-label="Social links"><span></span><span></span><span></span><span></span></div>
    <p class="copyright">&copy;2015 Kestra Total Relief. All rights reserved.</p>
  </div>
</footer>

</body>
</html>
```